Upbeat Accouting Package Flyer

I am looking for a 1 page (front, or front and back) flyer that will become our marketing for our accounting services. We are looking for something a little different and we are catering to the small retail shop owners. We have 3 accounting packages we would like to display and then some add-ons. I have included our logo that must be included in the design. I have uploaded the accounting package information as well.
Target Market(s)
Small Retail Shop Owners
Industry/Entity Type
Accounting
Colors
Designer to choose colors to be used in the design.
Requirements
Must have
- A casual feel. We are not your typical accountants who are very professional and "stuffy". I want it to feel like we are all family.
Nice to have
- I would like to incorporate some sort of retail theme.
- We have a couple of taglines we like to use and it would be great if they could be included. They are "We know you CAN do the accounting, but do you WANT to?" and "We allow you to get back to what's important."
Should not have
- Typical stock accounting photos of people shaking hands, large office buildings, etc.

```html
<!DOCTYPE html>
<html lang="en">
<head>
<meta charset="utf-8">
<title>Brightledger Accounting Packages Flyer</title>
<link href="https://fonts.googleapis.com/css2?family=Oswald:wght@300;400&family=Montserrat:wght@400;500;600;700&display=swap" rel="stylesheet">
<style>
  :root {
    --cyan: #1bb8dc;
    --cyan-light: #5fd3ef;
    --charcoal: #3d3d3f;
    --ink: #4a4a4c;
    --muted: #6d6d70;
    --paper: #ffffff;
  }
  * { margin: 0; padding: 0; box-sizing: border-box; }
  html, body { width: 768px; height: 1200px; overflow: hidden; background: var(--paper); }
  body { font-family: 'Montserrat', sans-serif; color: var(--ink); }
  .flyer { position: relative; width: 768px; height: 1200px; overflow: hidden; background: var(--paper); }
  .shapes { position: absolute; inset: 0; }

  .brand { position: absolute; left: 44px; top: 36px; }
  .brand-name { font-family: 'Montserrat', sans-serif; font-weight: 600; font-size: 44px; color: var(--charcoal); letter-spacing: 0.5px; line-height: 1; }
  .brand-sub { font-family: 'Montserrat', sans-serif; font-weight: 500; font-size: 11px; color: var(--cyan); letter-spacing: 0.5px; margin-top: 5px; text-align: right; }

  .hero-photo { position: absolute; left: 0; top: 123px; width: 640px; height: 310px;
    background: linear-gradient(110deg, #2e3236 0%, #5a5f66 30%, #b9a99a 55%, #e9e3dc 80%, #f4f1ec 100%); }

  .tagline { position: absolute; left: 0; top: 292px; width: 474px; height: 109px; background: rgba(27,184,220,0.92); padding: 14px 28px; color: #fff; }
  .tagline h1 { font-family: 'Oswald', sans-serif; font-weight: 300; font-size: 25px; line-height: 1.2; text-transform: uppercase; }
  .tagline p { font-size: 15px; margin-top: 6px; letter-spacing: 0.3px; }

  .section-title { position: absolute; left: 24px; top: 443px; font-family: 'Oswald', sans-serif; font-weight: 300; font-size: 25px; color: #fff; text-transform: uppercase; }

  .package { position: absolute; left: 0; width: 768px; }
  .package-icon { position: absolute; left: 18px; top: -8px; width: 46px; height: 46px; border-radius: 50%; background: #fff; border: 3px solid var(--cyan); }
  .package-name { position: absolute; left: 75px; top: 0; font-weight: 700; font-size: 15px; color: var(--cyan); text-transform: uppercase; }
  .package-name span { font-weight: 500; color: var(--muted); }
  .features { position: absolute; list-style: none; font-size: 10.5px; color: var(--muted); line-height: 1.25; }
  .features li { position: relative; padding-left: 12px; margin-bottom: 10.5px; }
  .features li::before { content: ""; position: absolute; left: 0; top: 4px; width: 4px; height: 4px; border-radius: 50%; background: var(--cyan); }
  .features.left { left: 80px; width: 300px; }
  .features.right { left: 395px; width: 320px; }

  .develop { top: 523px; }
  .grow { top: 646px; }
  .relax { top: 825px; }
  .develop .features { top: 36px; }
  .grow .features, .relax .features { top: 31px; }

  .additional { position: absolute; left: 26px; top: 1062px; color: #fff; }
  .additional h2 { font-size: 15px; font-weight: 700; text-transform: uppercase; letter-spacing: 0.5px; }
  .additional h2 span { color: var(--cyan); }
  .addon-list { position: absolute; list-style: none; font-size: 10.5px; line-height: 1.3; color: #fff; }
  .addon-list li { position: relative; padding-left: 12px; margin-bottom: 12px; }
  .addon-list li::before { content: ""; position: absolute; left: 0; top: 4px; width: 4px; height: 4px; border-radius: 50%; background: var(--cyan); }
  .addon-list.first { left: 0; top: 38px; width: 230px; }
  .addon-list.second { left: 240px; top: 38px; width: 200px; }

  .website { position: absolute; right: 16px; top: 1136px; font-weight: 700; font-size: 22px; color: #fff; letter-spacing: 2px; }
</style>
</head>
<body>
<main class="flyer">
  <svg class="shapes" width="768" height="1200" viewBox="0 0 768 1200" aria-hidden="true">
    <polygon points="495,0 640,0 768,380 768,433 620,433" fill="#1bb8dc" opacity="0.9"/>
    <polygon points="560,0 768,0 768,433 700,433" fill="#3fc6e6" opacity="0.55"/>
    <polygon points="629,0 768,0 675,153" fill="#3d3d3f"/>
    <polygon points="0,437 369,437 340,482 0,482" fill="#3d3d3f"/>
    <rect x="0" y="487" width="39" height="511" fill="#1bb8dc"/>
    <polygon points="0,998 480,998 768,1160 768,1200 0,1200" fill="#3d3d3f"/>
    <polygon points="768,971 768,1200 250,1200" fill="#1bb8dc"/>
  </svg>

  <div class="hero-photo" role="img" aria-label="Photo of hands typing on a laptop at a bright desk"></div>

  <header class="brand">
    <div class="brand-name">brightledger</div>
    <div class="brand-sub">TAX AND ACCOUNTING INC.</div>
  </header>

  <section class="tagline">
    <h1>We know you can do the accounting,<br>but do you want to?</h1>
    <p>We allow you to get back to what's important</p>
  </section>

  <h2 class="section-title">Accounting Packages:</h2>

  <section class="package develop">
    <svg class="package-icon" viewBox="0 0 46 46" aria-hidden="true"><circle cx="20" cy="18" r="8" fill="none" stroke="#1bb8dc" stroke-width="2.5"/><rect x="16" y="27" width="8" height="6" fill="#3d3d3f"/></svg>
    <h3 class="package-name">Develop</h3>
    <ul class="features left">
      <li>$300/mo when paid annually $325/mo billed monthly</li>
      <li>LedgerLeaf Online subscription</li>
      <li>Free accounting setup</li>
    </ul>
    <ul class="features right">
      <li>Weekly transaction processing</li>
      <li>Monthly account reconciliation (up to 2 accounts)</li>
      <li>Monthly financial statements by the 15th of the month</li>
    </ul>
  </section>

  <section class="package grow">
    <svg class="package-icon" viewBox="0 0 46 46" aria-hidden="true"><rect x="11" y="24" width="5" height="10" fill="#3d3d3f"/><rect x="18" y="18" width="5" height="16" fill="#1bb8dc"/><rect x="25" y="12" width="5" height="22" fill="#3d3d3f"/></svg>
    <h3 class="package-name">Grow</h3>
    <ul class="features left">
      <li>$550/mo billed annually; $575/mo billed monthly</li>
      <li>LedgerLeaf Online subscription</li>
      <li>Free accounting setup</li>
      <li>Weekly transaction processing</li>
      <li>Monthly account reconciliation (up to 4 accounts)</li>
    </ul>
    <ul class="features right">
      <li>Monthly financial statements by the 10th of the month</li>
      <li>Client portal access for document sharing</li>
      <li>1 Custom Report</li>
      <li>Accounts Payable</li>
      <li>Monthly Scorecard (customized metric tracking for your business)</li>
    </ul>
  </section>

  <section class="package relax">
    <svg class="package-icon" viewBox="0 0 46 46" aria-hidden="true"><circle cx="20" cy="13" r="4" fill="#1bb8dc"/><rect x="17" y="19" width="6" height="15" rx="2" fill="#3d3d3f"/></svg>
    <h3 class="package-name">Relax <span>(We've got this)</span></h3>
    <ul class="features left">
      <li>$850/mo billed annually; $875/mo billed monthly</li>
      <li>LedgerLeaf Online subscription</li>
      <li>Free accounting setup</li>
      <li>Weekly transaction processing</li>
      <li>Monthly account reconciliation (up to 5-10 accounts)</li>
      <li>Monthly financial statements by the 5th of the month</li>
    </ul>
    <ul class="features right">
      <li>Client portal access for document sharing</li>
      <li>2 Custom Reports</li>
      <li>Accounts Payable</li>
      <li>Invoicing and accounts receivable</li>
      <li>Weekly Scorecard (customized metric tracking for your business)</li>
    </ul>
  </section>

  <section class="additional">
    <h2><span>Additional</span> Options</h2>
    <ul class="addon-list first">
      <li>Payroll – 1-10 employees $85/mo;<br>11-30 employees $175/mo</li>
      <li>Sales tax - $30/mo per state</li>
    </ul>
    <ul class="addon-list second">
      <li>Corporate taxes $50/mo</li>
      <li>Owner taxes - $25/mo</li>
    </ul>
  </section>

  <div class="website">www.brightledgerkc.com</div>
</main>
</body>
</html>
```